Top Construction Software Co Needs a New Magazine Ad Design for 2013

Founded in 1986, PVTR is the market leader for innovative software solutions for the heavy civil construction industry. Our suite of products, including the bestsellers CrestQuote® and CrestCrew®, are used by more than 40,000 workers every day to improve their proficiency at estimating, job management, resource management, safety and equipment maintenance. PVTR also offers new mobile applications and cloud computing services so companies can work on a wide array of devices including laptops, tablets and smartphones.

In addition to high quality software, PVTR is best known for providing world-class customer service, and for its friendly, employee-ownership culture. We offer a full range of professional support options to help customers maximize their software investment including implementation planning, training and INSTANT 24/7 phone support.

Project description

We are creating a new magazine ad campaign for 2013 and need a full page and 1/3 page ad for this campaign.

The ad concept is Work Smarter, and we will provide 1 tip in each ad along with a case study of how a construction company can work smarter this year to save money, be more efficient or profitable.

Each ad will feature a "Work Smarter Tip # xx" headline, a sub-heading that contains the actual tip, a construction image that relates to the tip, a case study with bullet points about a company that has done the tip successfully and the results, an offer to download a free report with all of our 40 Work Smarter tips from a landing page, and our logo with branding elements.

The ad will typically run as a 1/3 page ad approximately 4" x 5", but we would like both a full page and 1/3 page design for the ad.

PVTR Brand personality traits - Innovative, market leader, competent, professional, masculine, friendly, and helpful. We've been in business for 27 years, and we are known for our world-class customer support and friendly helpful employees.
Updates

I've added a new logo file that has a square logo and a horizontal logo.  You can use either in the ad.

The text in the case study is a little long, and everyone seems to have a little trouble fitting it in the design.  Feel free to cut the last 2 or 3 bullets in your design, and I will make the text work with the size you give me.

Target Market(s)

Construction company executives, estimators, project managers, equipment managers, and IT support. We mainly target US and Canadian customers.

Industry/Entity Type

Construction

Requirements
Must have
• Ad title- "Work Smarter Tip #6"
Tip- Replace paper timecards with easy mobile apps
Image- Construction image related to the tip. Would like the tip potentially on the image, but open to suggestions. Just need the ad to be eye-catching to readers.
Case Study - Provide a case study of a company that implemented the tip with their results. This needs to be easy to read, and stand out from the ad.
Logo - Must use our company logo and it should be very visible.
Free Report - Want a strong call-to-action offer for the free report. See the attached word document for the copywriting for the ad elements.
Very important - the ad must be eye-catching. Something that will make readers want to read the tip while breezing through a magazine, while still being professional and matching our branding elements. Call to Action for free report should also be very visible.

Brand colors - Green PMS 356 and black are our dominant colors, can use yellow and orange (C=0, M=48, Y=98, K=0) as accent colors.
Nice to have
• We want to be viewed as helpful, industry leader, professional.

I attached a .pdf document of an ad created by a graphic designer that is good, but we are willing to pay to get more creative designs. The .pdf shows basically what we are looking for, but would like more creativity and something that will stop readers. Also, the designer changed our logo which we don't like so use the attached logo.
Should not have
• Feminine design - our industry is largely male construction workers.

Don't use script or goofy fonts
Don't change the logo, or put it in an image where it is not easily viewable.
Don't do something that is unprofessional like show a naked woman, etc.

```html
<!DOCTYPE html>
<html lang="en">
<head>
<meta charset="utf-8">
<title>PVTR – Work Smarter Tip #6</title>
<link rel="stylesheet" href="https://fonts.googleapis.com/css2?family=Exo+2:wght@600;700&family=Open+Sans:wght@400;700&display=swap">
<style>
  :root {
    --page: #000000;
    --ink: #1d1d1d;
    --brand-green: #139a43;
    --accent-yellow: #ffd100;
    --accent-orange: #f7941d;
    --cta-red: #e3212f;
    --panel-top: #b9ddf3;
    --panel-bottom: #ffffff;
    --white: #ffffff;
  }
  * { margin: 0; padding: 0; box-sizing: border-box; }
  html, body { width: 922px; height: 1200px; overflow: hidden; background: var(--page); }
  .ad {
    position: absolute; left: 100px; top: 100px; width: 722px; height: 1000px;
    overflow: hidden;
    background: linear-gradient(180deg, var(--panel-top) 467px, #dcedf8 700px, var(--panel-bottom) 880px);
    font-family: "Open Sans", Arial, sans-serif; color: var(--ink);
  }
  .hero-photo {
    position: absolute; left: 0; top: 0; width: 722px; height: 467px;
    background: linear-gradient(180deg, #9cc7ea 0%, #cfe3f2 38%, #b8b5a8 52%, #8c7a58 70%, #6f5e3f 100%);
  }
  .hero-photo .worker-tone {
    position: absolute; right: 0; top: 0; width: 260px; height: 467px;
    background: linear-gradient(160deg, #e8e8e8 0%, #b83a32 45%, #f07a22 80%, #c23a30 100%);
    opacity: .85;
  }
  .headline {
    position: absolute; left: 36px; top: 46px;
    font-family: "Exo 2", Arial, sans-serif; font-weight: 700; font-size: 36px; letter-spacing: -.2px;
    color: #161616;
  }
  .ribbon {
    position: absolute; left: 0;
    background: linear-gradient(90deg, var(--accent-orange), var(--accent-yellow) 55%);
    font-family: "Exo 2", Arial, sans-serif; font-weight: 600; color: #1b1b1b;
  }
  .tip-ribbon {
    top: 97px; width: 410px; height: 69px; padding: 6px 0 0 36px;
    font-size: 23px; line-height: 28px;
    clip-path: polygon(0 0, 100% 0, 88% 100%, 0 100%);
  }
  .case-ribbon {
    top: 473px; width: 272px; height: 44px; padding: 8px 0 0 54px;
    font-size: 23px; font-weight: 700; letter-spacing: .3px;
    clip-path: polygon(0 0, 100% 0, 86% 100%, 0 100%);
  }
  .case-company {
    position: absolute; left: 54px; top: 527px;
    font-family: "Exo 2", Arial, sans-serif; font-weight: 600; font-size: 19.5px;
  }
  .case-results {
    position: absolute; left: 54px; top: 563px; width: 570px;
    list-style: none; font-size: 15.5px; line-height: 18px; color: #2a2a2a;
  }
  .case-results li { position: relative; padding-left: 19px; margin-bottom: 5px; }
  .case-results li::before { content: "•"; position: absolute; left: 0; }
  .report-offer { position: absolute; left: 73px; top: 783px; }
  .report-offer h2 {
    font-family: "Exo 2", Arial, sans-serif; font-weight: 700; font-size: 20px; color: var(--cta-red);
  }
  .report-offer p { font-size: 15px; line-height: 19px; color: #222; }
  .brand-mark {
    position: absolute; left: 488px; top: 800px;
    display: flex; align-items: center; gap: 12px;
    font-family: "Exo 2", Arial, sans-serif; font-weight: 700; font-size: 64px; color: var(--brand-green);
  }
  .brand-mark .dot { width: 22px; height: 22px; background: var(--brand-green); }
  .footer-swoosh { position: absolute; left: 0; top: 860px; width: 722px; height: 140px; }
  .free-badge { position: absolute; left: 52px; top: 862px; width: 146px; height: 102px; }
  .free-badge svg { position: absolute; left: 0; top: 0; width: 146px; height: 102px; }
  .free-badge span {
    position: absolute; left: 0; width: 146px; text-align: center; color: var(--white);
    font-family: "Exo 2", Arial, sans-serif; font-weight: 700;
  }
  .free-badge .big { top: 21px; font-size: 32px; line-height: 34px; }
  .free-badge .small { top: 54px; font-size: 20px; line-height: 24px; }
  .web-address {
    position: absolute; left: 168px; top: 962px;
    font-weight: 700; font-size: 15.5px; color: var(--white); letter-spacing: .2px;
  }
</style>
</head>
<body>
<main class="ad">
  <div class="hero-photo" role="img" aria-label="Photo: construction foreman in hard hat and safety vest using a tablet app beside a highway bridge site">
    <div class="worker-tone"></div>
  </div>
  <h1 class="headline">Work Smarter - Tip #6</h1>
  <div class="ribbon tip-ribbon">Replace your paper timecards<br>with easy mobile apps</div>

  <div class="ribbon case-ribbon">CASE STUDY</div>
  <p class="case-company">Marlow Construction, an asphalt paving company in Abilene KS</p>
  <ul class="case-results">
    <li>Wanted to be able to monitor job profitability and<br>make the office more efficient.</li>
    <li>Implemented CrestCrew Mobile Apps in the field on SlateTabs.</li>
    <li>Foremen were initially resistant until they tried it, they realized the apps<br>were easy to learn and use.</li>
    <li>Eliminated double-entry of data, lost timecards, unreadable printing</li>
    <li>Now able to see if a job is over-running or under-running right away</li>
    <li>Receive timecards daily instead of weekly</li>
    <li>Reduced payroll time from 2 – 3 days to ½ a day</li>
  </ul>

  <div class="report-offer">
    <h2>40 Tips for Working Smarter</h2>
    <p>Download a free report with 40 tips,<br>case studies, and how-to guides.</p>
  </div>

  <div class="brand-mark"><span class="dot"></span>PVTR</div>

  <svg class="footer-swoosh" viewBox="0 0 722 140" aria-hidden="true">
    <path d="M0,15 C200,62 450,100 722,98 L722,140 L0,140 Z" fill="var(--brand-green)"/>
    <path d="M0,26 C200,72 450,104 722,92" fill="none" stroke="var(--accent-yellow)" stroke-width="5"/>
  </svg>

  <div class="free-badge">
    <svg viewBox="-75 -75 150 150" preserveAspectRatio="none" aria-hidden="true">
      <polygon fill="var(--cta-red)" stroke="var(--white)" stroke-width="2" points="74,0 60.8,12.1 68.4,28.3 51.5,34.5 52.3,52.3 34.5,51.5 28.3,68.4 12.1,60.8 0,74 -12.1,60.8 -28.3,68.4 -34.5,51.5 -52.3,52.3 -51.5,34.5 -68.4,28.3 -60.8,12.1 -74,0 -60.8,-12.1 -68.4,-28.3 -51.5,-34.5 -52.3,-52.3 -34.5,-51.5 -28.3,-68.4 -12.1,-60.8 0,-74 12.1,-60.8 28.3,-68.4 34.5,-51.5 52.3,-52.3 51.5,-34.5 68.4,-28.3 60.8,-12.1"/>
    </svg>
    <span class="big">FREE</span>
    <span class="small">Report</span>
  </div>

  <p class="web-address">www.pvtr.com/worksmart</p>
</main>
</body>
</html>
```